Box and Paper Bag Design
for exclusive line of prescriptions creams
Box and Paper Bag Design  - Health
Creative Brief
A design for the box (layout attached) and a promotional paper bag (no layout - see sample picture: 8" length, 7" high, 3.5" deep) - front and back designs will be fine. Both packages are for exclusive line of prescription creams. Should resemble expensive, high end, sophisticated and upscale style, yet THIS IS PRESCRIPTION MEDICATION - the packaging should resemble this also. FRONT: 1. Logo (attached) 2. Text: Professional Prescription Formula Dispensed Only By Physicians 3. On the bottom: e 30 ml / 1 fl.oz. Made in USA BACK: All the way on the bottom - try to fit into lower 1/4th of the space: Directions: Follow the directions of your prescribing Physician Cautions: For external use only - do not ingest. Avoid contact with open wounds. Avoid getting into eyes. Make sure skin is clean and dry before applying . Discontinue use if rash or discomfort occurs. Not for use by pregnant or lactating women. The packaging is NOT child resistant. KEEP AWAY FROM CHILDREN. If accidentally ingested seek medical help immediately. _________________________ We will be using various technics while printing the boxes: uv coating, spot foil etc See several samples of the designs I liked attached. Try to stick to conservative yet fresh colors: metallic, silver, gray , blue, green.
Health
Doctors, medical professionals and their patients.

```html
<!DOCTYPE html>
<html lang="en">
<head>
<meta charset="utf-8">
<title>Veridose – Prescription Cream Box</title>
<link href="https://fonts.googleapis.com/css2?family=Montserrat:wght@300;400&family=Open+Sans:wght@400;600&display=swap" rel="stylesheet">
<style>
  :root {
    --stage: #cfd0d2;
    --panel-white: #ffffff;
    --ray-blue: #cfe6f3;
    --lime: #a9cf2c;
    --lime-deep: #8fbb1c;
    --ink-white: #ffffff;
    --logo-grey: #4a4a4a;
    --logo-frame: #e4e4e4;
  }
  html, body {
    margin: 0;
    width: 1200px;
    height: 901px;
    overflow: hidden;
    background: radial-gradient(ellipse at 50% 45%, #e6e7e8 0%, var(--stage) 75%);
    font-family: "Open Sans", sans-serif;
  }
  .dieline {
    position: absolute;
    top: 180px;
    left: 200px;
    display: flex;
    gap: 40px;
  }
  .panel {
    position: relative;
    width: 380px;
    height: 540px;
    background: var(--panel-white);
    box-shadow: 0 10px 30px rgba(0,0,0,0.18);
    overflow: hidden;
  }
  .sunburst {
    position: absolute;
    left: 0; top: 0; right: 0;
    height: 360px;
    background: radial-gradient(circle at 50% 40%, #ffffff 0%, #f1f8fc 35%, var(--ray-blue) 100%);
  }
  .band {
    position: absolute;
    left: 0; right: 0; bottom: 0;
    height: 180px;
    background: var(--lime);
  }
  .logo-tile {
    position: absolute;
    width: 104px;
    height: 104px;
    background: var(--panel-white);
    border: 1px solid var(--logo-frame);
    display: flex;
    align-items: center;
    justify-content: center;
  }
  .logo-name {
    font-family: "Montserrat", sans-serif;
    font-weight: 300;
    font-size: 16px;
    letter-spacing: 3px;
    color: var(--logo-grey);
  }
  .front .logo-tile { left: 138px; top: 128px; }
  .claim {
    position: absolute;
    left: 30px;
    top: 40px;
    color: var(--ink-white);
    font-size: 12px;
    line-height: 1.5;
    letter-spacing: 0.6px;
    text-transform: uppercase;
    margin: 0;
  }
  .volume {
    position: absolute;
    left: 30px;
    top: 84px;
    color: var(--ink-white);
    font-size: 9px;
    letter-spacing: 0.5px;
    margin: 0;
  }
  .back .sunburst { height: 200px; }
  .back-field {
    position: absolute;
    left: 0; right: 0; bottom: 0;
    height: 340px;
    background: radial-gradient(circle at 20% 10%, var(--lime) 0%, var(--lime-deep) 100%);
  }
  .back .logo-tile { right: 26px; top: 30px; width: 84px; height: 84px; }
  .back .logo-name { font-size: 13px; letter-spacing: 2px; }
  .directions {
    position: absolute;
    left: 30px;
    right: 30px;
    bottom: 40px;
    color: var(--ink-white);
    font-size: 10px;
    line-height: 1.6;
    margin: 0;
  }
  .directions strong { font-weight: 600; }
</style>
</head>
<body>
  <main class="dieline">
    <section class="panel front">
      <div class="sunburst" role="img" aria-label="Pale blue radiating sunburst rays on white"></div>
      <div class="logo-tile"><span class="logo-name">VERIDOSE</span></div>
      <div class="band">
        <p class="claim">Professional Prescription Formula<br>Dispensed Only By Physicians</p>
        <p class="volume">&#8494; 30 ml / 1 fl.oz. Made in USA</p>
      </div>
    </section>
    <section class="panel back">
      <div class="sunburst" role="img" aria-label="Pale blue radiating sunburst rays on white"></div>
      <div class="back-field" role="img" aria-label="Lime green radiating sunburst rays"></div>
      <div class="logo-tile"><span class="logo-name">VERIDOSE</span></div>
      <p class="directions"><strong>Directions:</strong> Follow the directions of your prescribing physician. <strong>Cautions:</strong> For external use only, do not ingest. Avoid contact with open wounds and eyes. Discontinue use if rash or discomfort occurs. Keep away from children.</p>
    </section>
  </main>
</body>
</html>
```